Supplement Label Design Project

We need a rockstar graphic designer who can create a great supplement label for our product. Our product is called Titan Momentum and it is produced by BRIX470. There are many supplements out there and this design needs to stand out from all the rest, please ref. this link for all types of supplements in our same category: http://www.gymcratedepot.com/store/goalpreworkout.htm

Requirements:
- BRIX470 logo
- Product name: Titan Momentum
- By line: Build Rest Intake eXert with B R I X bold or standing out
- Space for nutritional facts, directions and product story copy
- Layout should be nutritional facts on left then product design in center and product story copy on right
- Label size, final cut size: 3.206" X 14" and 1.8" bleeds

Brand Style and Influence:
- Our site is www.BRIX470fitness.com
- Please reference the site to get a feel for our brand style and colors
- We like this companies product label designs: http://www.fibrowerks.com/
- We need to stand out from all the current supplements. We were thinking of using our homepage image of the guy lifting somehow in the design.
- Attached are the logo, flyers and images we have made to give you a look and feel.
- Really like the HDR style and look where it makes muscles look more intense

Target Market(s)

18-35, male, athlete, not necessarily a bodybuilder type more of an all round athlete like rigmoor

Industry/Entity Type

Graphic Designer

Requirements
Must have
• - BRIX470 logo

```html
<!DOCTYPE html>
<html lang="en">
<head>
<meta charset="utf-8">
<title>Titan Momentum Label – BRIX470</title>
<link rel="stylesheet" href="https://fonts.googleapis.com/css2?family=Russo+One&family=Open+Sans:wght@700&family=Arimo&display=swap">
<style>
  :root {
    --ink: #0b0d10;
    --smoke-dark: #15181b;
    --smoke-mid: #3a3d40;
    --smoke-light: #5a5d60;
    --brand-yellow: #f1cf3a;
    --label-blue: #a8c2d6;
    --copy-white: #f2f2f2;
    --photo-deep: #1d2a36;
    --photo-mid: #4d6272;
  }
  html, body {
    margin: 0;
    padding: 0;
    width: 1200px;
    height: 275px;
    overflow: hidden;
    background: var(--ink);
  }
  .label {
    position: relative;
    width: 1200px;
    height: 275px;
    overflow: hidden;
    background:
      radial-gradient(ellipse 260px 150px at 560px 150px, var(--smoke-light) 0%, transparent 70%),
      radial-gradient(ellipse 300px 170px at 820px 110px, var(--smoke-mid) 0%, transparent 75%),
      radial-gradient(ellipse 200px 140px at 700px 240px, var(--smoke-mid) 0%, transparent 75%),
      linear-gradient(90deg, var(--ink) 0%, var(--smoke-dark) 30%, var(--smoke-dark) 75%, var(--ink) 100%);
    font-family: "Arimo", Arial, sans-serif;
  }

  /* Left panel: nutritional facts, set vertically */
  .facts {
    position: absolute;
    left: 0;
    top: 275px;
    width: 275px;
    height: 185px;
    transform-origin: top left;
    transform: rotate(-90deg);
    box-sizing: border-box;
    padding: 3px 6px 0 2px;
  }
  .facts__title {
    margin: 0 0 2px;
    font-family: "Russo One", sans-serif;
    font-size: 14px;
    letter-spacing: 0.5px;
    color: var(--label-blue);
    line-height: 20px;
  }
  .facts__copy {
    margin: 0;
    font-size: 11.5px;
    line-height: 19.5px;
    color: var(--copy-white);
    text-align: justify;
  }

  /* Hero photo of the athlete */
  .hero-photo {
    position: absolute;
    left: 185px;
    top: 0;
    width: 250px;
    height: 275px;
    background:
      radial-gradient(ellipse 90px 110px at 110px 110px, var(--photo-mid) 0%, transparent 80%),
      linear-gradient(180deg, var(--photo-deep) 0%, #24323d 60%, var(--ink) 100%);
  }

  /* Brand name in place of the mark */
  .brand-name {
    position: absolute;
    left: 215px;
    top: 160px;
    margin: 0;
    font-family: "Russo One", sans-serif;
    font-size: 58px;
    line-height: 70px;
    letter-spacing: 2px;
    color: var(--brand-yellow);
  }

  /* Product title block */
  .product-title {
    position: absolute;
    left: 487px;
    top: 26px;
    margin: 0;
    font-family: "Russo One", sans-serif;
    font-size: 30px;
    line-height: 36px;
    color: var(--brand-yellow);
    letter-spacing: 0.5px;
  }
  .byline {
    position: absolute;
    left: 489px;
    top: 64px;
    margin: 0;
    font-family: "Open Sans", sans-serif;
    font-weight: 700;
    font-size: 18px;
    line-height: 26px;
    color: var(--copy-white);
    letter-spacing: 0.5px;
  }
  .byline__brand {
    color: var(--brand-yellow);
    letter-spacing: 3px;
    text-decoration: underline;
    text-decoration-thickness: 2px;
    text-underline-offset: 5px;
  }

  /* Right panel: product story */
  .story-photo {
    position: absolute;
    left: 945px;
    top: 0;
    width: 100px;
    height: 92px;
    background: radial-gradient(ellipse 45px 46px at 50px 44px, #6b6f72 0%, #2a2d30 60%, transparent 100%);
  }
  .story {
    position: absolute;
    left: 940px;
    top: 90px;
    width: 250px;
  }
  .story__title {
    margin: 0 0 4px;
    text-align: right;
    font-family: "Russo One", sans-serif;
    font-size: 13px;
    line-height: 20px;
    color: var(--label-blue);
  }
  .story__copy {
    margin: 0;
    font-size: 11.5px;
    line-height: 19.5px;
    color: var(--copy-white);
    text-align: justify;
  }
</style>
</head>
<body>
<main class="label">
  <section class="facts">
    <h2 class="facts__title">NUTRITIONAL FACTS</h2>
    <p class="facts__copy">Lorem ipsum dolor sit amet, consectetur adipiscing elit. Sed molestie neque eget lectus pulvinar euismod. Nulla sed magna elit, at lacinia tortor. Nullam elit velit, tristique eget blandit eget, pulvinar in velit. Nam vehicula magna ornare orci ultricies luctus. Praesent in libero risus. Aenean sit amet nisi arcu, cursus blandit odio. Nulla</p>
  </section>

  <div class="hero-photo" role="img" aria-label="Athlete in a crouched ready stance, gritty blue-toned HDR photograph"></div>

  <p class="brand-name">BRIX470</p>

  <h1 class="product-title">TITAN MOMENTUM</h1>
  <p class="byline">BUILD REST INTAKE eXERT WITH <span class="byline__brand">B R I X</span></p>

  <div class="story-photo" role="img" aria-label="Athlete mid jump, small grayscale photograph"></div>

  <section class="story">
    <h2 class="story__title">PRODUCT STORY</h2>
    <p class="story__copy">Lorem ipsum dolor sit amet, consectetur adipiscing elit. Sed molestie neque eget lectus pulvinar euismod. Nulla sed magna elit, at lacinia tortor. Nullam elit velit, tristique eget blandit eget, pulvinar in velit. Nam vehicula magna ornare orci ultricies luctus. Praesent in libero risus. Aenean sit amet nisi arcu, cursus blandit odio. Nulla</p>
  </section>
</main>
</body>
</html>
```